Free Range Egg Farmer wants a Egg Carton Design

We need a design for Free Range Egg carton. Our company name is "BrookHaven The Craft of Growing"

We run a environmentally friendly farm in Fernhollow VIC and we produce Free Range Eggs and Pasture Fed Meats in open pasture.

We also run a farm stay business in a very high energy star rating house.
The farm guest participates in our farm activity such as looking after farm animals, maintaining the vegetable garden, cooking fresh food, Yoga and Meditation.

We would like to see designs with our logo and something alternative rather than a typical free range egg cartons.

The team had a meeting and came up with one idea.
"The meditating hen" with thought bubble which we can change the hen's thought by printing batch.
You could either use this idea or create your own.

I have attached 3 photos close to my image as examples.
I also have attached the typical free range egg cartons as examples.

Sticker size is attached. The sticker fits between the case closure system. So there is no need to make spaces for the closure gaps.
Please place Best Before stamp area at the top right corner of the main (middle) section.
Updates

I have post an update to my brief. Please have a look again. BrookHaven

Industry/Entity Type

Printing

Requirements
Must have
• Company name,
Address,
contact number,
facebook logo,
best before date (space to put the stamp on)
12 Free Range Eggs xxx g
Nutrition info

```html
<!DOCTYPE html>
<html lang="en">
<head>
<meta charset="utf-8">
<title>BrookHaven Free Range Egg Carton Label</title>
<link href="https://fonts.googleapis.com/css2?family=Leckerli+One&family=Ropa+Sans&display=swap" rel="stylesheet">
<style>
  :root {
    --page: #ffffff;
    --label-purple: #652d90;
    --ink-white: #ffffff;
    --accent-orange: #f7941d;
    --fold-line: #555555;
    --seal-dark: #3a3a3a;
  }
  html, body {
    margin: 0;
    padding: 0;
    width: 1200px;
    height: 1000px;
    overflow: hidden;
    background: var(--page);
  }
  .canvas {
    position: relative;
    width: 1200px;
    height: 1000px;
    background: var(--page);
    font-family: "Ropa Sans", sans-serif;
  }
  .label {
    position: absolute;
    left: 145px;
    top: 90px;
    width: 902px;
    height: 818px;
    background: var(--label-purple);
  }
  .fold-line {
    position: absolute;
    left: 0;
    width: 1200px;
    height: 0;
    border-top: 1.5px dashed var(--fold-line);
  }
  .fold-line--top { top: 277px; }
  .fold-line--bottom { top: 706px; }

  /* lid flap, printed upside down */
  .flap {
    position: absolute;
    left: 145px;
    top: 90px;
    width: 902px;
    height: 187px;
    transform: rotate(180deg);
  }
  .flap__seal {
    position: absolute;
    left: 39px;
    top: 27px;
    width: 140px;
    height: 140px;
    border-radius: 50%;
    background: var(--seal-dark);
    border: 2px solid var(--ink-white);
    box-sizing: border-box;
    display: flex;
    align-items: center;
    justify-content: center;
    color: var(--ink-white);
    font-size: 24px;
  }
  .nutrition {
    position: absolute;
    left: 204px;
    top: 32px;
    color: var(--ink-white);
    font-size: 22px;
    line-height: 25px;
  }
  .nutrition p { margin: 0; }

  /* main panel */
  .best-before {
    position: absolute;
    right: 183px;
    top: 314px;
    color: var(--accent-orange);
    font-size: 32px;
    letter-spacing: 1px;
  }
  .hen-art {
    position: absolute;
    left: 200px;
    top: 290px;
    width: 345px;
    height: 400px;
    border-radius: 40% 40% 30% 30%;
    background: radial-gradient(ellipse at 45% 60%, #ffffff 0%, #ffffff 55%, rgba(247,148,29,0.85) 100%);
  }
  .thought {
    position: absolute;
    left: 545px;
    top: 345px;
    width: 340px;
    height: 250px;
  }
  .pack-size {
    position: absolute;
    right: 168px;
    top: 616px;
    font-family: "Leckerli One", cursive;
    color: var(--ink-white);
    font-size: 35px;
    line-height: 1.2;
  }

  /* base panel */
  .brand {
    position: absolute;
    left: 165px;
    top: 730px;
    color: var(--ink-white);
    font-family: "Leckerli One", cursive;
  }
  .brand__name {
    margin: 0;
    font-size: 82px;
    line-height: 96px;
    font-weight: 400;
  }
  .brand__tagline {
    margin: 0;
    font-size: 46px;
    line-height: 60px;
    font-weight: 400;
  }
  .contact {
    position: absolute;
    right: 170px;
    top: 740px;
    text-align: right;
    color: var(--ink-white);
    font-size: 26px;
    line-height: 30.5px;
    font-style: normal;
  }
  .contact p { margin: 0; }
  .contact__social {
    display: inline-flex;
    align-items: center;
    gap: 8px;
    margin-top: 2px;
    font-size: 29px;
  }
  .contact__social-mark {
    width: 30px;
    height: 30px;
    background: var(--accent-orange);
    border-radius: 3px;
  }
</style>
</head>
<body>
<div class="canvas">
  <div class="label"></div>
  <div class="fold-line fold-line--top"></div>
  <div class="fold-line fold-line--bottom"></div>

  <section class="flap">
    <div class="nutrition">
      <p>Nutrition info:</p>
      <p>fdhfjgik</p>
      <p>hgjdhgjkghjk</p>
      <p>gfjdkhgjg</p>
      <p>hgfjdbgjhg</p>
    </div>
    <div class="flap__seal">BrookHaven</div>
  </section>

  <div class="best-before">Best Before 01/07/2014</div>

  <div class="hen-art" role="img" aria-label="Illustration of a white hen with orange wings and tail, eyes closed, meditating"></div>

  <svg class="thought" viewBox="0 0 340 250" aria-hidden="true">
    <g fill="#ffffff">
      <circle cx="7" cy="8" r="3"/>
      <circle cx="27" cy="17" r="6"/>
      <circle cx="52" cy="33" r="11"/>
      <circle cx="140" cy="80" r="58"/>
      <circle cx="225" cy="70" r="55"/>
      <circle cx="280" cy="130" r="55"/>
      <circle cx="70" cy="145" r="58"/>
      <circle cx="150" cy="190" r="52"/>
      <circle cx="230" cy="190" r="50"/>
      <ellipse cx="180" cy="140" rx="115" ry="80"/>
    </g>
  </svg>

  <div class="pack-size">12 Free Range Eggs xxx g</div>

  <header class="brand">
    <h1 class="brand__name">BrookHaven</h1>
    <p class="brand__tagline">The Craft of Growing</p>
  </header>

  <address class="contact">
    <p>Address: ghkfkdhklfd</p>
    <p>ndjgngkjfdg</p>
    <p>Fernhollow VIC</p>
    <p>0400 555 019</p>
    <p class="contact__social"><span class="contact__social-mark"></span>BrookHavenCraftofGrowing</p>
  </address>
</div>
</body>
</html>
```